Marbrook Jewelers New Website Design

This project is to provide a new design for an existing website. The existing website is marbrookjewelers dot com . I have created a overview document that outlines all the details for the project. I do not need the design to be converted into HTML. I have a team for that already so please don't ask. I have a lot of images .. too many to upload here so they are on my dev server located at pinfernstudio com slash marbrook slash assets

Number of Pages Required

1 page

```html
<!DOCTYPE html>
<html lang="en">
<head>
<meta charset="utf-8">
<title>Marbrook Jewelers</title>
<link href="https://fonts.googleapis.com/css2?family=Jost:wght@300;400;500&display=swap" rel="stylesheet">
<style>
:root{
  --teal:#5b9aa0;
  --teal-soft:#7fb1b5;
  --ink:#1d1d1d;
  --muted:#555;
  --line:#d8d8d8;
  --black:#000;
  --white:#fff;
}
*{box-sizing:border-box;margin:0;padding:0}
html,body{width:1200px;height:4615px;overflow:hidden}
body{font-family:'Jost',sans-serif;color:var(--ink);background:var(--white);position:relative}
.abs{position:absolute}
.topbar{left:0;top:0;width:1200px;height:43px;background:var(--teal);color:var(--white);font-size:14px;text-align:center;line-height:43px;font-weight:300}
.util{top:122px;font-size:13px;letter-spacing:.3px;text-transform:uppercase}
.util small{text-transform:none;color:var(--muted);font-size:13px}
.call{left:197px;top:122px;font-size:13px;line-height:20px}
.call span{color:var(--muted)}
.brand{left:450px;top:120px;width:300px;text-align:center;font-size:44px;font-weight:400;color:var(--ink);letter-spacing:1px}
.brand-dot{left:592px;top:62px;width:20px;height:20px;border-radius:50%;background:var(--teal-soft)}
.nav{left:0;top:229px;width:1200px;height:50px;border-top:1px solid var(--line);border-bottom:1px solid var(--line)}
.nav a{position:absolute;top:13px;font-size:15px;color:var(--ink);text-decoration:none}
.nav a.active{color:var(--teal)}
.nav .bar{position:absolute;left:80px;top:-2px;width:78px;height:3px;background:var(--teal)}
.hero-left{left:0;top:279px;width:602px;height:509px;background:linear-gradient(135deg,#6aa4a9,#5b9aa0)}
.hero-right{left:602px;top:279px;width:598px;height:509px;background:linear-gradient(135deg,#555,#bbb 55%,#eee)}
.eyebrow{font-size:13px;letter-spacing:.5px;text-transform:uppercase}
.hero-left .eyebrow{position:absolute;left:86px;top:134px;color:var(--white)}
.hero-title{position:absolute;left:86px;top:157px;color:var(--white);font-size:47px;line-height:58px;font-weight:500;letter-spacing:.5px}
.btn-light{position:absolute;background:var(--white);color:var(--teal);border-radius:24px;font-size:13px;text-transform:uppercase;text-align:center}
.btn-dark{position:absolute;background:var(--black);color:var(--white);border-radius:24px;font-size:13px;text-transform:uppercase;text-align:center}
.label{position:absolute;left:0;width:1200px;text-align:center;color:var(--teal);font-size:13px;text-transform:uppercase}
.h2{position:absolute;left:0;width:1200px;text-align:center;font-size:36px;font-weight:400}
.service{position:absolute;width:290px;text-align:center}
.service h3{font-size:16px;font-weight:400;letter-spacing:.5px;margin-top:24px}
.service p{font-size:13px;line-height:17px;color:var(--muted);margin-top:14px;padding:0 10px}
.vdiv{position:absolute;top:1096px;height:50px;border-left:2px dashed #888}
.card{position:absolute;width:238px;background:var(--white);box-shadow:0 0 14px rgba(0,0,0,.09);text-align:center}
.card .ph{position:absolute;border-radius:4px}
.card .nm{position:absolute;left:0;width:100%;font-size:15px}
.card .pr{position:absolute;left:0;width:100%;font-size:14px;color:var(--muted)}
.res-h{left:688px;top:1893px;font-size:36px}
.res-p{left:688px;width:430px;font-size:13px;line-height:21px;color:#333}
.gift{left:0;top:2382px;width:1200px;height:548px;background:linear-gradient(120deg,#5b969b,#6ea7ab 50%,#5a9398)}
.gift h2{position:absolute;left:0;top:110px;width:1200px;text-align:center;color:var(--white);font-size:36px;font-weight:400}
.gift p{position:absolute;left:262px;width:676px;text-align:center;color:var(--white);font-size:13px;line-height:21px}
.gal{position:absolute;top:3781px;width:267px;height:285px}
.footer{left:0;top:4187px;width:1200px;height:428px;background:var(--black);color:var(--white)}
.footer h4{position:absolute;top:80px;font-size:20px;font-weight:400}
.footer .lk{position:absolute;font-size:14px}
.footer .rule{position:absolute;left:86px;top:328px;width:1028px;border-top:1px solid #555}
.footer .copy{position:absolute;left:86px;top:356px;font-size:14px}
.social{position:absolute;top:353px;width:28px;height:28px;border-radius:50%;background:var(--white)}
</style>
</head>
<body>

<div class="abs topbar">Together we'll find a piece that speaks from the heart.</div>

<div class="abs util" style="left:86px">
  <svg width="14" height="14" viewBox="0 0 14 14" style="vertical-align:-2px;margin-right:6px"><circle cx="6" cy="6" r="4.5" fill="none" stroke="#1d1d1d" stroke-width="1.3"/><line x1="9.3" y1="9.3" x2="13" y2="13" stroke="#1d1d1d" stroke-width="1.3"/></svg>Search
</div>
<div class="abs call">CALL US: <span>555-014-2287(Phone)</span><br><span style="padding-left:65px">888-555-0194(Toll Free)</span></div>
<div class="abs brand-dot"></div>
<div class="abs brand">Marbrook<div style="font-size:11px;letter-spacing:6px;color:var(--teal);margin-top:-4px">JEWELERS</div></div>
<div class="abs util" style="left:874px">Login</div>
<div class="abs util" style="left:946px">Wishlist</div>
<div class="abs util" style="left:1037px">
  <svg width="13" height="14" viewBox="0 0 13 14" style="vertical-align:-2px;margin-right:4px"><path d="M1 4h11v9H1z" fill="none" stroke="#1d1d1d" stroke-width="1.2"/><path d="M4 4V3a2.5 2.5 0 0 1 5 0v1" fill="none" stroke="#1d1d1d" stroke-width="1.2"/></svg>Cart (0)
</div>

<nav class="abs nav">
  <span class="bar"></span>
  <a class="active" style="left:90px">Company</a>
  <a style="left:184px">Custom Jewelery Services <svg width="10" height="6" viewBox="0 0 10 6"><path d="M1 1l4 4 4-4" fill="none" stroke="#1d1d1d"/></svg></a>
  <a style="left:389px">Jewelery Repair Services</a>
  <a style="left:587px">Resources</a>
  <a style="left:688px">Showcase</a>
  <a style="left:784px">Gallery</a>
  <a style="left:863px">Engraving &amp; Trophies</a>
  <a style="left:1042px">Gift Ideas</a>
</nav>

<section class="abs hero-left">
  <div class="eyebrow">Marbrook Jewelers</div>
  <h1 class="hero-title">Say It with a Stone<br>and leave her<br>speechless</h1>
  <div class="btn-light" style="left:86px;top:357px;width:127px;height:44px;line-height:44px">Shop Now</div>
</section>
<div class="abs hero-right" role="img" aria-label="Black and white photo of two joined hands wearing wedding rings"></div>

<div class="label" style="top:904px">Marbrook Jewelers</div>
<h2 class="h2" style="top:923px">Custom Jewelery Services &amp; Repairs</h2>

<div class="service" style="left:102px;top:1015px">
  <svg width="56" height="52" viewBox="0 0 56 52"><circle cx="22" cy="32" r="16" fill="#cfe3e5"/><path d="M14 12l28 28M42 12L14 40" stroke="#1d1d1d" stroke-width="2" fill="none"/><circle cx="12" cy="42" r="4" fill="none" stroke="#1d1d1d" stroke-width="2"/><circle cx="22" cy="42" r="4" fill="none" stroke="#1d1d1d" stroke-width="2"/></svg>
  <h3>JEWELRY REPAIR</h3>
  <p>Jewelry was meant to be worn, not sit in a drawer. Bring your broken rings, necklaces, earrings and watches to your trusted hometown jeweler.</p>
</div>
<div class="service" style="left:453px;top:1015px">
  <svg width="56" height="52" viewBox="0 0 56 52"><circle cx="22" cy="30" r="16" fill="#cfe3e5"/><rect x="24" y="6" width="10" height="40" fill="none" stroke="#1d1d1d" stroke-width="2"/><path d="M24 14h5M24 22h5M24 30h5M24 38h5M34 10h8v6h-8" stroke="#1d1d1d" stroke-width="2" fill="none"/></svg>
  <h3>SIZING</h3>
  <p>Your first sizing is free when you purchase your ring at Marbrook Jewelers. If you need a ring sized, whether you bought it from us or not, we can help you find the size that fits.</p>
</div>
<div class="service" style="left:804px;top:1015px">
  <svg width="56" height="52" viewBox="0 0 56 52"><circle cx="22" cy="30" r="16" fill="#cfe3e5"/><path d="M10 18l8-10h20l8 10-18 26z M10 18h36 M18 8l10 36 10-36" stroke="#1d1d1d" stroke-width="2" fill="none" stroke-linejoin="round"/></svg>
  <h3>CUSTOM DESIGN</h3>
  <p>If you've inherited jewelry you'll never wear, we can recreate an entirely new piece while preserving the sentimental value of it.</p>
</div>
<div class="vdiv" style="left:423px"></div>
<div class="vdiv" style="left:775px"></div>

<div class="label" style="top:1309px">Marbrook Jewelers</div>
<h2 class="h2" style="top:1328px">Features Items</h2>

<div class="card" style="left:86px;top:1409px;height:285px"><div class="ph" role="img" aria-label="Silver bracelet watch with dark face" style="left:39px;top:70px;width:160px;height:50px;background:linear-gradient(90deg,#aaa,#555 50%,#aaa)"></div><div class="nm" style="top:177px">Marbrook Watch</div><div class="pr" style="top:205px">$ 50.00 - $ 60.00</div></div>
<div class="card" style="left:349px;top:1409px;height:285px"><div class="ph" role="img" aria-label="Rose gold diamond bangle" style="left:39px;top:60px;width:160px;height:70px;background:radial-gradient(ellipse,#fff 52%,#d99a7e 56%,#c8805f 62%,#fff 66%)"></div><div class="nm" style="top:177px">Gold + Diamond Bracelets</div><div class="pr" style="top:205px">$ 50.00 - $ 60.00</div></div>
<div class="card" style="left:613px;top:1409px;height:285px"><div class="ph" role="img" aria-label="White gold crossover diamond ring" style="left:49px;top:50px;width:140px;height:90px;background:radial-gradient(ellipse,#fff 35%,#ccc 50%,#999 62%,#fff 70%)"></div><div class="nm" style="top:177px">Gold + Diamond Rings</div><div class="pr" style="top:205px">$ 50.00 - $ 60.00</div></div>
<div class="card" style="left:876px;top:1409px;height:285px"><div class="ph" role="img" aria-label="White gold ring with red heart gemstone" style="left:59px;top:55px;width:120px;height:90px;background:radial-gradient(ellipse at 50% 65%,#8a1d2a 12%,#fff 20%,#ccc 45%,#fff 60%)"></div><div class="nm" style="top:178px">Gold + Gemstone Rings</div><div class="pr" style="top:206px">$ 50.00 - $ 60.00</div></div>

<div class="btn-dark" style="left:535px;top:1737px;width:128px;height:45px;line-height:45px">View All</div>

<div class="abs" role="img" aria-label="Close-up of a gold chevron ring set with diamonds" style="left:86px;top:1904px;width:471px;height:268px;background:linear-gradient(135deg,#8c8a84,#d4d0c4 50%,#a69c80)"></div>
<div class="abs" role="img" aria-label="Rose gold halo ring with morganite on black background" style="left:451px;top:2013px;width:167px;height:247px;background:radial-gradient(circle at 50% 55%,#c9a48e 0,#6a5a50 25%,#1e1e1e 55%)"></div>
<div class="abs res-h">Resources</div>
<p class="abs res-p" style="top:1957px">Lorem Ipsum is simply dummy text of the printing and typesetting industry. Lorem Ipsum has been the industry's standard dummy text ever since the 1500s</p>
<p class="abs res-p" style="top:2036px;color:var(--muted)">when an unknown printer took a galley of type and scrambled it to make a type specimen book. It has survived not only five centuries, but also the leap into electronic typesetting, remaining essentially unchanged. It was popularised in the 1960s with the release of Letraset sheets containing Lorem Ipsum passages, and more recently with desktop publishing software like Quill PageSetter including versions of Lorem Ipsum.</p>
<div class="btn-dark" style="left:690px;top:2210px;width:127px;height:47px;line-height:47px">Learn More</div>

<section class="abs gift" role="img" aria-label="Teal-tinted photo of a jeweler working at the bench">
  <h2>Gift Ideas</h2>
  <p style="top:185px">Lorem Ipsum is simply dummy text of the printing and typesetting industry. Lorem Ipsum has been the industry's standard dummy text ever since the 1500s</p>
  <p style="top:248px">when an unknown printer took a galley of type and scrambled it to make a type specimen book. It has survived not only five centuries, but also the leap into electronic typesetting, remaining essentially unchanged. It was popularised in the 1960s with the release of Letraset sheets containing Lorem Ipsum passages, and more recently with desktop publishing software like Quill PageSetter including versions of Lorem Ipsum.</p>
  <div class="btn-light" style="left:535px;top:380px;width:128px;height:43px;line-height:43px">Shop Now</div>
</section>

<div class="label" style="top:3046px">Marbrook Jewelers</div>
<h2 class="h2" style="top:3067px">Engraving &amp; Trophies</h2>

<div class="card" style="left:86px;top:3147px;height:320px"><div class="ph" role="img" aria-label="Three post hockey trophy" style="left:89px;top:40px;width:60px;height:160px;background:linear-gradient(90deg,#6b1010,#c9a040 50%,#6b1010)"></div><div class="nm" style="top:233px">3 post hockey trophy</div><div class="pr" style="top:261px">$ 590.00 - $ 800.00</div></div>
<div class="card" style="left:349px;top:3147px;height:320px"><div class="ph" role="img" aria-label="Clear acrylic award on blue base" style="left:59px;top:50px;width:120px;height:140px;background:linear-gradient(180deg,#e6eef2,#b9c8d0 85%,#1d3f6e 86%)"></div><div class="nm" style="top:233px">Acrylic Award</div><div class="pr" style="top:261px">$ 590.00 - $ 800.00</div></div>
<div class="card" style="left:613px;top:3147px;height:320px"><div class="ph" role="img" aria-label="Flame-shaped acrylic award on black base" style="left:74px;top:55px;width:90px;height:140px;background:linear-gradient(180deg,#f1f1ef,#ddd 85%,#222 86%)"></div><div class="nm" style="top:233px">Acrylic Award 2</div><div class="pr" style="top:261px">$ 590.00 - $ 800.00</div></div>
<div class="card" style="left:876px;top:3147px;height:320px"><div class="ph" role="img" aria-label="Walnut award plaque with engraved navy plate" style="left:64px;top:55px;width:110px;height:145px;background:radial-gradient(#1c2c48 45%,#6d3b1e 47%)"></div><div class="nm" style="top:234px">Award Plaques</div><div class="pr" style="top:262px">$ 590.00 - $ 800.00</div></div>

<div class="btn-dark" style="left:535px;top:3519px;width:128px;height:45px;line-height:45px">View All</div>

<div class="label" style="top:3682px">Marbrook Jewelers</div>
<h2 class="h2" style="top:3703px">Gallery</h2>

<div class="gal" role="img" aria-label="Dragonfly pendant with colored gemstones" style="left:29px;background:linear-gradient(135deg,#f2eee0,#d8cfb6)"></div>
<div class="gal" role="img" aria-label="Glass cross on white satin" style="left:322px;background:linear-gradient(135deg,#c8c2bc,#8f8680)"></div>
<div class="gal" role="img" aria-label="Engraving machine at work" style="left:616px;background:linear-gradient(135deg,#8a8a8a,#2e2e2e)"></div>
<div class="gal" role="img" aria-label="Gold ring with coral and amethyst stones" style="left:908px;background:linear-gradient(135deg,#a7b2b8,#6e7a80)"></div>

<footer class="abs footer">
  <h4 style="left:86px">Main Menu</h4>
  <div class="lk" style="left:86px;top:138px">Company</div>
  <div class="lk" style="left:86px;top:174px">Custom Jewelery Services</div>
  <div class="lk" style="left:86px;top:210px">Jewelery Repair Services</div>
  <div class="lk" style="left:86px;top:244px">Resources</div>
  <div class="lk" style="left:306px;top:138px">Showcase</div>
  <div class="lk" style="left:306px;top:174px">Gallery</div>
  <div class="lk" style="left:306px;top:210px">Engraving &amp; Trophies</div>
  <div class="lk" style="left:306px;top:244px">Gift Ideas</div>

  <h4 style="left:535px">Category</h4>
  <div class="lk" style="left:535px;top:138px">Rings</div>
  <div class="lk" style="left:535px;top:174px">Quickshops</div>
  <div class="lk" style="left:535px;top:210px">Pendants</div>
  <div class="lk" style="left:535px;top:244px">Earrings</div>
  <div class="lk" style="left:664px;top:138px">Diamonds</div>
  <div class="lk" style="left:664px;top:174px">Gemstones</div>

  <h4 style="left:820px">Contact Info</h4>
  <div class="lk" style="left:822px;top:138px">Location: 48 Elm St N, Fairhaven, MN</div>
  <div class="lk" style="left:822px;top:181px;line-height:26px">Phone: 555-014-2287<br>888-555-0194 (Toll Free)</div>
  <div class="lk" style="left:822px;top:243px">Store Hours:&nbsp; Mon-Fri: 8:00 AM - 5:00PM</div>

  <div class="rule"></div>
  <div class="copy">©2022 Marbrook Jewelers: Minnesota Jeweler. All Rights Reserved.</div>
  <span class="social" style="left:1041px"></span>
  <span class="social" style="left:1084px"></span>
</footer>

</body>
</html>
```